ZENITH conference Slide Deck

This is a conference for our team that will be 3 days of discussions on how to build our business in the middle of these challenging time. Its a bit of a battle and so we are going with a red and grey/black these although I am open to your interpretation. I will include a few graphics that we have started on to show you the look. But I am just getting started, INSPIRE ME! The screen will be 100' across the front of the room and these decks will show on each side and I will reformat for the middle 1X6 screen as needed. I have the AI file of the logo if you need it. I don't see where to upload it here.

Target Market(s)

our top producers

Industry/Entity Type

Real Estate Agent

Font styles to use
Sans Serif

Colors
ec1f27

Requirements
Must have
• Depth, creativity

```html
<!DOCTYPE html>
<html lang="en">
<head>
<meta charset="utf-8">
<title>ZENITH Conference Slide Deck</title>
<link href="https://fonts.googleapis.com/css2?family=Titillium+Web:wght@300;700&family=Open+Sans:wght@400;700&display=swap" rel="stylesheet">
<style>
:root{
  --red:#ec1f27;
  --deep-red:#b3141a;
  --ink:#0b0b0b;
  --char:#3a3a3a;
  --card:#2a2a2a;
  --grey:#9a9a9a;
  --white:#ffffff;
}
*{box-sizing:border-box;margin:0;padding:0}
html,body{width:900px;height:1200px;overflow:hidden;background:var(--white)}
.board{
  width:900px;height:1200px;padding:22px;
  display:grid;grid-template-columns:repeat(3,260px);
  grid-auto-rows:146px;column-gap:39px;row-gap:22px;
}
.slide{
  position:relative;overflow:hidden;
  box-shadow:0 6px 14px rgba(0,0,0,.35);
  font-family:'Open Sans',sans-serif;color:var(--white);
}
.dark{background:linear-gradient(180deg,var(--char) 0%,var(--ink) 100%)}
.black{background:#000}
.red{background:var(--red)}
.title{
  position:absolute;left:23px;
  font:700 15px/1 'Titillium Web',sans-serif;text-transform:uppercase;letter-spacing:.2px;
}
.accent{color:var(--red)}
.foot-logo{
  position:absolute;left:23px;bottom:1px;z-index:3;
  font:700 5px/1 'Titillium Web',sans-serif;color:var(--red);letter-spacing:.4px;
}
.page-no{position:absolute;right:9px;bottom:2px;font-size:3px;color:var(--grey);z-index:3}
.strip{position:absolute;left:0;right:0;bottom:0;height:7px;background:#111;z-index:2}
.tiny{font-size:3.6px;line-height:1.55}
.chev{position:absolute;fill:none;stroke-linecap:butt;stroke-linejoin:miter}
.chev.c-red{stroke:var(--red)}
.chev.c-black{stroke:#000}
.chev.c-grey{stroke:#8a8a8a}
.chev.c-white{stroke:#e6e6e6}
.chev.c-maroon{stroke:#9c1218}
.photo{position:absolute}

/* cover */
.cover .photo{inset:0;background:radial-gradient(ellipse at 75% 45%,#6a6a6a 0%,#333 45%,#0c0c0c 100%)}
.cover-rule{position:absolute;left:14px;top:0;bottom:0;width:3px;background:var(--red)}
.cover-logo{position:absolute;left:33px;top:40px;font:700 27px/1 'Titillium Web',sans-serif;color:var(--red);letter-spacing:1px}
.cover-title{position:absolute;left:33px;top:74px;font:700 12px/1.25 'Titillium Web',sans-serif;text-transform:uppercase}

/* talk */
.talk .title{top:36px;font-size:14px}
.talk-body{position:absolute;left:23px;top:84px;width:220px;font-size:3.8px;line-height:1.65;color:#ddd}
.talk-body strong{display:block;font-size:4.4px;color:var(--white);margin-bottom:2px}

/* event */
.event .title{top:16px;font-size:14px}
.event-panel{position:absolute;left:185px;top:0;right:0;bottom:0;background:var(--red)}
.day{position:absolute;left:23px;width:160px;height:28px}
.day .photo{left:0;top:0;width:67px;height:28px;background:linear-gradient(135deg,#1b2a6b,#6e5a8a 60%,#2a2a3a)}
.day h3{position:absolute;left:75px;top:0;font:700 4.5px/1 'Open Sans',sans-serif;color:var(--red)}
.day ol{position:absolute;left:80px;top:7px;font-size:3.2px;line-height:1.75;color:#ddd}

/* speakers */
.speakers .title{top:58px;left:21px;font-size:14px;line-height:1.1}
.speaker{position:absolute;top:0;bottom:0;width:47.7px}
.speaker .photo{inset:0}
.speaker .name{position:absolute;left:3px;top:102px;font-size:4.6px}
.speaker .bio{position:absolute;left:3px;top:109px;width:42px;font-size:2.9px;line-height:1.5;color:#ddd}
.speaker.s1{left:117px}
.speaker.s1 .photo{background:linear-gradient(180deg,#1a34b8 0%,#2c2c6a 55%,#3a3a3a 100%)}
.speaker.s2{left:164.7px}
.speaker.s2 .photo{background:linear-gradient(180deg,#5b4030 0%,#8a6a5a 45%,#e0465a 75%,#ec1f27 100%)}
.speaker.s3{left:212.4px}
.speaker.s3 .photo{background:linear-gradient(180deg,#6a6a5a 0%,#4a4a4a 55%,#2a2a2a 100%)}

/* agenda */
.agenda .title{top:12px;line-height:1.05}
.agenda-rule{position:absolute;top:52px;height:1px;background:var(--red)}
.time{position:absolute;top:59px;font-size:4.4px;color:#ddd}
.slot{position:absolute;top:73px;width:52px;height:61px;background:var(--card);padding:6px 5px}
.slot h4{font:700 4.4px/1.15 'Open Sans',sans-serif;margin-bottom:4px}
.slot ol{padding-left:4px;font-size:3px;line-height:1.6;color:#aaa}
.slot li::marker{color:var(--red)}
.tick-sep{position:absolute;top:58px;width:1px;height:8px;background:#555}

/* who / what headers */
.big-head{position:absolute;left:23px;top:60px;font:700 19px/1 'Titillium Web',sans-serif;text-transform:uppercase}
.what-head{top:63px;font-size:20px;text-shadow:0 2px 4px rgba(0,0,0,.45)}
.what-head .shade{color:#2a0406}
.who-text .title,.what-text .title{top:15px;line-height:1.05}
.cols{position:absolute;left:23px;top:63px;width:220px;display:flex;gap:8px}
.cols ul{flex:1;padding-left:5px;font-size:3.5px;line-height:1.55;text-align:justify}
.cols li{margin-bottom:3px}
.who-text .cols ul{color:var(--red)}
.what-text .cols ul{color:var(--white)}

/* lorem headline */
.lorem .title{top:30px;font-size:15px}
.bullets-right{position:absolute;left:110px;top:62px;width:120px;padding-left:5px;font-size:3.6px;line-height:1.55;color:var(--red)}
.bullets-right li{margin-bottom:2px}

/* house */
.house .side{position:absolute;left:0;top:0;bottom:0;width:17px;background:#151515;z-index:2}
.house .side-logo{position:absolute;left:3px;bottom:22px;transform:rotate(-90deg);transform-origin:left bottom;font:700 5px/1 'Titillium Web',sans-serif;color:var(--red);white-space:nowrap}
.house .photo{left:17px;top:0;right:0;bottom:0;background:linear-gradient(180deg,#3a3550 0%,#56453a 50%,#2a1f18 75%,#1a2530 100%)}
.house-title{position:absolute;right:19px;top:13px;text-align:right;font:700 14px/1.05 'Titillium Web',sans-serif;text-transform:uppercase;z-index:2}
.house-list{position:absolute;left:153px;top:51px;list-style:none;font:700 6.2px/1 'Open Sans',sans-serif;letter-spacing:.6px;z-index:2}
.house-list li{margin-bottom:13px}
.house-list li::before{content:"\2022";margin-right:3px}
.house-mark{position:absolute;left:126px;bottom:0;width:19px;height:10px;background:var(--red);z-index:2}

/* speaker quote */
.quote .photo{left:10px;top:16px;width:110px;height:118px;border-radius:46% 38% 40% 52%;background:radial-gradient(ellipse at 45% 40%,#d96a6a 0%,#1d2d9a 45%,#0f1020 100%)}
.right-title{position:absolute;right:21px;top:21px;text-align:right;font:700 15px/1.05 'Titillium Web',sans-serif;text-transform:uppercase}
.quote-body{position:absolute;right:21px;top:64px;width:84px;text-align:justify;font-size:3.5px;line-height:1.4;color:var(--red)}
.quote-body p{margin-bottom:2px}

/* should do */
.should .photo{left:0;top:22px;width:145px;height:102px;background:linear-gradient(135deg,#1a1a1a,#8a8a8a 45%,#2a2a2a 80%);clip-path:polygon(6% 16%,100% 0,96% 88%,12% 100%,0 55%)}
.say-box{position:absolute;left:152px;width:85px;height:28px;background:var(--red);padding:4px 6px}
.say-box h5{font:700 4.4px/1 'Open Sans',sans-serif;margin-bottom:3px}
.say-box p{font-size:3px;line-height:1.5}
.say-link{position:absolute;left:135px;width:17px;height:1px;background:var(--red)}
.say-link::before{content:"";position:absolute;left:-1px;top:-1px;width:3px;height:3px;border-radius:50%;background:var(--red)}

/* options */
.options .title{top:15px;font-size:14px}
.options-panel{position:absolute;left:164px;top:0;right:0;bottom:0;background:var(--red)}
.option{position:absolute;left:23px;width:170px;height:27px}
.option .photo{left:108px;top:0;width:66px;height:27px}
.option .msg{position:absolute;left:0;top:2px;width:104px;text-align:right}
.option h5{font:700 4.2px/1 'Open Sans',sans-serif;color:var(--red);margin-bottom:2px}
.option p{font-size:2.9px;line-height:1.5;color:var(--red)}
.o1 .photo{background:linear-gradient(180deg,#9aa8b8,#5a6a7a 55%,#e8a020 80%,#3a4a5a)}
.o2 .photo{background:linear-gradient(135deg,#2a4aa8,#e8c020 50%,#1a1a1a)}
.o3 .photo{background:linear-gradient(135deg,#e8e8e8,#c8b8a8 50%,#6a8ab8)}

/* two alternatives */
.alt-tri{position:absolute;inset:0}
.alt .title{top:15px;line-height:1.05}
.alt-box{position:absolute;left:20px;width:203px;height:30px;display:flex;align-items:center}
.alt-box::before{content:"";position:absolute;left:0;top:-1px;width:63px;height:2px}
.alt-box.b1{top:61px;background:#000}
.alt-box.b1::before{background:var(--red)}
.alt-box.b2{top:99px;background:var(--red)}
.alt-box.b2::before{background:#d9d9d9}
.alt-box h5{width:57px;text-align:right;font:700 5px/1.2 'Open Sans',sans-serif;padding-right:2px}
.alt-box.b1 h5{color:var(--white)}
.alt-box p{margin-left:12px;width:125px;font-size:3.3px;line-height:1.7}

/* doing */
.doing .title{top:15px}
.dir{position:absolute;height:34px;background:#000;display:flex;align-items:center;gap:5px;padding:0 4px}
.dir::before{content:"";position:absolute;left:0;top:-1px;width:50px;height:2px;background:var(--red)}
.dir h5{font:700 6px/1.05 'Titillium Web',sans-serif;color:var(--red);width:58px;text-align:right}
.dir p{font-size:2.8px;line-height:1.5;color:var(--red);width:48px}
.dir.d1{left:20px;top:58px;width:117px}
.dir.d1 h5{text-align:left}
.dir.d2{left:143px;top:58px;width:117px}
.dir.d3{left:81px;top:98px;width:124px}
.dir-block{position:absolute;left:205px;top:98px;width:55px;height:34px;background:var(--red)}

/* market */
.market .title{top:15px}
.stat{position:absolute;top:54px;width:100px}
.stat .num{font:300 17px/1 'Titillium Web',sans-serif;white-space:nowrap}
.stat p{margin-top:3px;font-size:3.4px;line-height:1.35;text-align:justify}
.stat.st1{left:20px}
.stat.st2{left:145px}

/* take action */
.action .title{top:15px;line-height:1.05}
.steps{position:absolute;left:23px;top:62px;width:218px;display:grid;grid-template-columns:1fr 1fr;column-gap:9px;row-gap:5px;list-style:none}
.steps li{display:flex;gap:3px;font-size:3.5px;line-height:1.5}
.steps b{font:400 7px/1 'Open Sans',sans-serif}

/* solutions */
.solutions .title{top:15px;line-height:1.05}
.sol{position:absolute;top:65px;width:56px;height:75px;background:#111;padding:6px 5px}
.sol::before{content:"";position:absolute;left:0;top:-1px;width:46px;height:2px;background:var(--red)}
.sol h5{font:700 6px/1.1 'Titillium Web',sans-serif;color:var(--red);margin-bottom:8px}
.sol p{font-size:2.8px;line-height:1.5;color:var(--red)}
.sol.x1{left:20px}.sol.x2{left:81px}.sol.x3{left:143px}
.sol.x4{left:205px;background:var(--red)}
.sol.x4::before{background:#000}
.sol.x4 h5,.sol.x4 p{color:var(--white)}

/* vision */
.vision-head{position:absolute;left:23px;top:40px;font:700 19px/1 'Titillium Web',sans-serif;text-transform:uppercase;color:#111}
.ticks{position:absolute;left:82px;top:68px;width:128px;list-style:none;font-size:3.6px;line-height:1.5}
.ticks li{position:relative;padding-left:5px;margin-bottom:3px}
.ticks li::before{content:"\2713";position:absolute;left:0;top:0}
</style>
</head>
<body>
<main class="board">

  <!-- 1 cover -->
  <section class="slide cover">
    <div class="photo" role="img" aria-label="Black and white photo of hands gripping a rope in a tug of war"></div>
    <span class="cover-rule"></span>
    <div class="cover-logo">ZENITH</div>
    <h1 class="cover-title">Business in the middle<br>of challenging time</h1>
  </section>

  <!-- 2 talk -->
  <section class="slide dark talk">
    <svg class="chev c-red" style="left:203px;top:13px" width="10" height="18" viewBox="0 0 10 18"><polyline points="2,2 8,9 2,16" stroke-width="3.5"/></svg>
    <svg class="chev c-black" style="left:216px;top:32px" width="18" height="30" viewBox="0 0 18 30"><polyline points="3,3 14,15 3,27" stroke-width="6"/></svg>
    <svg class="chev c-grey" style="left:193px;top:54px" width="14" height="22" viewBox="0 0 14 22"><polyline points="2,2 10,11 2,20" stroke-width="4.5"/></svg>
    <h2 class="title">Let´s talk about<br><span class="accent">our conference</span></h2>
    <div class="talk-body">
      <strong>Lorem Ipsum is simply dummy the printing and typesetting industry.</strong>
      Our three days focus on growth, grit and clear goals for every agent in the room. Each session shares tools, stories and plans that help top producers lead their markets through change and build stronger teams for the year ahead.
    </div>
    <span class="foot-logo">ZENITH</span><span class="page-no">2</span>
  </section>

  <!-- 3 event -->
  <section class="slide dark event">
    <div class="event-panel"></div>
    <svg class="chev c-white" style="left:203px;top:13px" width="12" height="20" viewBox="0 0 12 20"><polyline points="2,2 9,10 2,18" stroke-width="3.5"/></svg>
    <svg class="chev c-black" style="left:218px;top:36px" width="18" height="30" viewBox="0 0 18 30"><polyline points="3,3 14,15 3,27" stroke-width="6"/></svg>
    <svg class="chev c-maroon" style="left:194px;top:57px" width="14" height="24" viewBox="0 0 14 24"><polyline points="2,2 10,12 2,22" stroke-width="4.5"/></svg>
    <h2 class="title"><span class="accent">The</span> event:</h2>
    <div class="day" style="top:38px">
      <div class="photo" role="img" aria-label="Photo of a speaker on stage under blue light"></div>
      <h3>Day 1 The Leadership Team</h3>
      <ol><li>Opening talk and goals</li><li>Team workshop session</li><li>Evening network mixer</li></ol>
    </div>
    <div class="day" style="top:71px">
      <div class="photo" role="img" aria-label="Photo of a presenter in front of a projected screen" style="background:linear-gradient(135deg,#e8e2da,#8a6a5a 55%,#3a3a3a)"></div>
      <h3>Day 2 Responsible Approach</h3>
      <ol><li>Opening talk and goals</li><li>Team workshop session</li><li>Evening network mixer</li></ol>
    </div>
    <div class="day" style="top:105px">
      <div class="photo" role="img" aria-label="Photo of a speaker seated on stage before an audience" style="background:linear-gradient(135deg,#c8d0c8,#5a5a4a 55%,#2a2a2a)"></div>
      <h3>Day 3 Low Product Prices</h3>
      <ol><li>Opening talk and goals</li><li>Team workshop session</li><li>Evening network mixer</li></ol>
    </div>
    <span class="foot-logo">ZENITH</span>
  </section>

  <!-- 4 speakers -->
  <section class="slide dark speakers">
    <svg class="chev c-white" style="left:19px;top:8px" width="12" height="20" viewBox="0 0 12 20"><polyline points="2,2 9,10 2,18" stroke-width="3.5"/></svg>
    <svg class="chev c-black" style="left:34px;top:33px" width="18" height="30" viewBox="0 0 18 30"><polyline points="3,3 14,15 3,27" stroke-width="6"/></svg>
    <svg class="chev c-maroon" style="left:8px;top:52px" width="14" height="24" viewBox="0 0 14 24"><polyline points="2,2 10,12 2,22" stroke-width="4.5"/></svg>
    <h2 class="title">The<br>speakers</h2>
    <div class="speaker s1">
      <div class="photo" role="img" aria-label="Photo of a speaker with a microphone on a blue lit stage"></div>
      <div class="name">Dale Hart</div><p class="bio">Leads growth for top teams</p>
    </div>
    <div class="speaker s2">
      <div class="photo" role="img" aria-label="Photo of a presenter in a suit gesturing, tinted red"></div>
      <div class="name">Ryan Cole</div><p class="bio">Leads growth for top teams</p>
    </div>
    <div class="speaker s3">
      <div class="photo" role="img" aria-label="Photo of a speaker seated beside a projection screen"></div>
      <div class="name">Sam Price</div><p class="bio">Leads growth for top teams</p>
    </div>
    <span class="foot-logo">ZENITH</span>
  </section>

  <!-- 5 agenda -->
  <section class="slide dark agenda">
    <h2 class="title"><span class="accent">Conference</span><br>agenda</h2>
    <span class="agenda-rule" style="left:44px;right:0"></span>
    <span class="time" style="left:49px">09:00am</span>
    <span class="tick-sep" style="left:99px"></span>
    <span class="time" style="left:104px">09:30am</span>
    <span class="tick-sep" style="left:155px"></span>
    <span class="time" style="left:160px">09:40am</span>
    <div class="slot" style="left:44px"><h4>Welcome<br>Message</h4><ol><li>Open with a short note on goals.</li><li>Questions and a quick break.</li></ol></div>
    <div class="slot" style="left:100px"><h4>About us</h4><ol><li>Open with a short note on goals.</li><li>Questions and a quick break.</li></ol></div>
    <div class="slot" style="left:156px"><h4>Section</h4><ol><li>Open with a short note on goals.</li><li>Questions and a quick break.</li></ol></div>
    <span class="foot-logo">ZENITH</span><span class="page-no">4</span>
  </section>

  <!-- 6 agenda continued -->
  <section class="slide dark agenda">
    <span class="agenda-rule" style="left:0;width:205px"></span>
    <span class="time" style="left:46px">10:00am</span>
    <span class="tick-sep" style="left:97px"></span>
    <span class="time" style="left:102px">10:20am</span>
    <span class="tick-sep" style="left:152px"></span>
    <span class="time" style="left:157px">11:30am</span>
    <div class="slot" style="left:45px"><h4>Our Team</h4><ol><li>Open with a short note on goals.</li><li>Questions and a quick break.</li></ol></div>
    <div class="slot" style="left:99px"><h4>Infographics</h4><ol><li>Open with a short note on goals.</li><li>Questions and a quick break.</li></ol></div>
    <div class="slot" style="left:153px"><h4>Contact us</h4><ol><li>Open with a short note on goals.</li><li>Questions and a quick break.</li></ol></div>
    <span class="foot-logo">ZENITH</span><span class="page-no">5</span>
  </section>

  <!-- 7 who we are -->
  <section class="slide black">
    <h2 class="big-head"><span class="accent">Who</span> we are<span class="accent">:</span></h2>
    <span class="foot-logo">ZENITH</span><span class="page-no">7</span>
  </section>

  <!-- 8 who we are text -->
  <section class="slide dark who-text">
    <h2 class="title"><span class="accent">Who</span><br>we are<span class="accent">:</span></h2>
    <div class="cols">
      <ul><li>We are a team of agents who lead local markets with care, data and drive.</li><li>We share tools and stories so every producer grows in hard times.</li></ul>
      <ul><li>We are a team of agents who lead local markets with care, data and drive.</li><li>We share tools and stories so every producer grows in hard times.</li></ul>
    </div>
    <span class="foot-logo">ZENITH</span><span class="page-no">8</span>
  </section>

  <!-- 9 what we do -->
  <section class="slide red">
    <h2 class="big-head what-head"><span class="shade">What</span> we do:</h2>
    <span class="strip"></span>
    <span class="foot-logo">ZENITH</span><span class="page-no">9</span>
  </section>

  <!-- 10 what we do text -->
  <section class="slide red what-text">
    <h2 class="title" style="color:#111">What<br><span style="color:var(--white)">we do:</span></h2>
    <div class="cols">
      <ul><li>We help clients buy and sell homes with clear advice and fast service.</li><li>We train agents to win listings and keep clients for life.</li></ul>
      <ul><li>We help clients buy and sell homes with clear advice and fast service.</li><li>We train agents to win listings and keep clients for life.</li></ul>
    </div>
    <span class="strip"></span>
    <span class="foot-logo">ZENITH</span><span class="page-no">10</span>
  </section>

  <!-- 11 lorem ipsum dolor sit -->
  <section class="slide dark lorem">
    <h2 class="title"><span class="accent">Lorem ipsum</span> dolor sit</h2>
    <ul class="bullets-right">
      <li>Build plans that hold in any market.</li>
      <li>Track leads and follow up each week.</li>
      <li>Share wins and lessons with the team.</li>
      <li>Lead with care.</li>
    </ul>
    <span class="foot-logo">ZENITH</span><span class="page-no">18</span>
  </section>

  <!-- 12 house -->
  <section class="slide house">
    <div class="side"><span class="side-logo">ZENITH</span></div>
    <div class="photo" role="img" aria-label="Photo of a modern two storey house with lit windows and a pool at dusk"></div>
    <h2 class="house-title">Lorem ipsum has<br>been the industry's</h2>
    <ul class="house-list">
      <li>Low product prices</li>
      <li>Powerful SMM</li>
      <li>Leadership team</li>
      <li>Responsible approach</li>
    </ul>
    <span class="house-mark"></span>
  </section>

  <!-- 13 speaker quote -->
  <section class="slide dark quote">
    <div class="photo" role="img" aria-label="Cut-out photo of a speaker with a microphone over a blue brush stroke"></div>
    <h2 class="right-title"><span class="accent">Lorem ipsum</span><br>dolor sit</h2>
    <div class="quote-body">
      <p>Real growth starts with people who stay calm, plan well and serve clients with honest advice every day.</p>
      <p>Set clear goals.</p>
    </div>
    <span class="foot-logo">ZENITH</span><span class="page-no">17</span>
  </section>

  <!-- 14 should do -->
  <section class="slide dark should">
    <div class="photo" role="img" aria-label="Black and white photo of a boxer training at a heavy bag"></div>
    <h2 class="right-title" style="right:24px;top:20px"><span class="accent">What we</span><br>should do</h2>
    <span class="say-link" style="top:81px"></span>
    <div class="say-box" style="top:68px"><h5>We have something to say</h5><p>A short note that explains this point.</p></div>
    <span class="say-link" style="top:112px"></span>
    <div class="say-box" style="top:99px"><h5>We have something to say</h5><p>A short note that explains this point.</p></div>
    <span class="foot-logo">ZENITH</span><span class="page-no">12</span>
  </section>

  <!-- 15 options -->
  <section class="slide dark options">
    <div class="options-panel"></div>
    <h2 class="title"><span class="accent">3</span> options <span class="accent">slide</span></h2>
    <div class="option o1" style="top:38px">
      <div class="msg"><h5>Main Message</h5><p>A short line that sums up this option for the team.</p></div>
      <div class="photo" role="img" aria-label="Photo of a person in a yellow jacket looking over a lake"></div>
    </div>
    <div class="option o2" style="top:72px">
      <div class="msg"><h5>Main Message</h5><p>A short line that sums up this option for the team.</p></div>
      <div class="photo" role="img" aria-label="Photo of a foot in a yellow boot stepping forward"></div>
    </div>
    <div class="option o3" style="top:105px">
      <div class="msg"><h5>Main Message</h5><p>A short line that sums up this option for the team.</p></div>
      <div class="photo" role="img" aria-label="Photo of two colleagues planning at a whiteboard"></div>
    </div>
    <span class="foot-logo">ZENITH</span>
  </section>

  <!-- 16 two alternatives -->
  <section class="slide dark alt">
    <svg class="alt-tri" width="260" height="146" viewBox="0 0 260 146"><polygon points="160,0 260,0 260,125" fill="#ec1f27"/></svg>
    <h2 class="title"><span class="accent">Two</span> alternatives<br>for <span class="accent">slide design</span></h2>
    <div class="alt-box b1"><h5>We have something<br>to say</h5><p>Lorem Ipsum has been the industry's standard dummy text ever since the 1500s, when an unknown printer took a galley</p></div>
    <div class="alt-box b2"><h5>We have something<br>to say</h5><p>Lorem Ipsum has been the industry's standard dummy text ever since the 1500s, when an unknown printer took a galley</p></div>
    <span class="foot-logo">ZENITH</span><span class="page-no">13</span>
  </section>

  <!-- 17 doing -->
  <section class="slide dark doing">
    <h2 class="title"><span class="accent">What are</span> we doing</h2>
    <div class="dir d1"><h5>The first creative direction</h5><p>A short note on this direction.</p></div>
    <div class="dir d2"><h5>The second creative direction</h5><p>A short note on this direction.</p></div>
    <div class="dir d3"><h5>Third creative direction</h5><p>A short note on this direction.</p></div>
    <span class="dir-block"></span>
    <span class="foot-logo">ZENITH</span><span class="page-no">11</span>
  </section>

  <!-- 18 market -->
  <section class="slide dark market">
    <h2 class="title">Market validation</h2>
    <div class="stat st1"><div class="num">630,000 Mill</div><p>Homes sold by our members in the last year across all regions we serve.</p></div>
    <div class="stat st2"><div class="num">456,700 Mill</div><p>Homes sold by our members in the last year across all regions we serve.</p></div>
    <span class="foot-logo">ZENITH</span><span class="page-no">21</span>
  </section>

  <!-- 19 take action -->
  <section class="slide red action">
    <h2 class="title" style="color:#111">Take<br>action</h2>
    <ol class="steps">
      <li><b>1.</b><span>Set one clear goal for the next quarter.</span></li>
      <li><b>4.</b><span>Join a study group with two top producers.</span></li>
      <li><b>2.</b><span>Call ten past clients every single week now.</span></li>
      <li><b>5.</b><span>Review your numbers each Friday before you leave.</span></li>
      <li><b>3.</b><span>Share one market update with your whole list.</span></li>
      <li><b>6.</b><span>Thank one partner each day for their support.</span></li>
    </ol>
    <span class="strip"></span>
    <span class="foot-logo">ZENITH</span><span class="page-no">22</span>
  </section>

  <!-- 20 solutions -->
  <section class="slide dark solutions">
    <svg class="chev c-red" style="left:203px;top:13px" width="10" height="18" viewBox="0 0 10 18"><polyline points="2,2 8,9 2,16" stroke-width="3.5"/></svg>
    <svg class="chev c-black" style="left:216px;top:32px" width="18" height="30" viewBox="0 0 18 30"><polyline points="3,3 14,15 3,27" stroke-width="6"/></svg>
    <svg class="chev c-grey" style="left:193px;top:54px" width="14" height="22" viewBox="0 0 14 22"><polyline points="2,2 10,11 2,20" stroke-width="4.5"/></svg>
    <h2 class="title">Our<br><span class="accent">solutions</span></h2>
    <div class="sol x1"><h5>Leadership<br>team</h5><p>A short note on this solution.</p></div>
    <div class="sol x2"><h5>Responsible<br>approach</h5><p>A short note on this solution.</p></div>
    <div class="sol x3"><h5>Low product<br>prices</h5><p>A short note on this solution.</p></div>
    <div class="sol x4"><h5>Powerful<br>SMM</h5><p>A short note on this solution.</p></div>
    <span class="foot-logo">ZENITH</span><span class="page-no">16</span>
  </section>

  <!-- 21 vision -->
  <section class="slide red">
    <h2 class="vision-head">Share the vision:</h2>
    <ul class="ticks">
      <li>We grow together, lead with care and keep our promise to each client.</li>
      <li>We adapt fast, learn from every deal and stay close to our communities.</li>
      <li>We build a brand of trust that lasts long after the market turns.</li>
    </ul>
    <span class="strip"></span>
    <span class="foot-logo">ZENITH</span><span class="page-no">19</span>
  </section>

</main>
</body>
</html>
```